Sharper Daily Habits Qorafone App

I am looking to create an Qorafone app (support Qorafone 5 and above) that will inspire and empower the app user to be more productive through a creative, interative and simplistic user experience that teaches the 10 topics related to "Sharper Daily Habits". Please see attached zip files for the 10 topic as PDF files and 20 posters (20 jpg files) which include a quote related to the content bundle’s topic.

Target Market(s)

working professionals who desire to be more productive in their ways of doing

Industry/Entity Type

It Support

Font styles to use
Sans Serif

Colors
33a6d7
0255a3
9bcb3b
cadf82
33b8a4

Requirements
Must have
• don't really wanna say "ebook" style app which would be below my expectation, i expect something more creative than an "ebook" app. i prefer you use your creativity to come up with the design but if you are a bit lost, please read below.
• some specs in my mind:
• - 10 flash cards design for each of the topic so they can be used in a carousel style menu (see sample app screenshot 1 - 1st screen to the left)
• - when presenting a topic, the background should be the same as the flash card of the topic (see sample app screenshot 2 - the right most screen)
• - at the bottom of the topic screen, a audio play/pause buttons bar should be presented as the app will play audible version for the article.
• - the fashion of the sample app screen shots shouldn't be followed as it is an ancient fashion reflecting the content. I expect the fashion of the app should be modern and reflect the topic "sharper daily habits"
• Screens required:
• - Main menu screen: carosoul style presenting the 10 topics using flash cards, should have a "play/pause" button to play the audible topic
• - Topic screen: presents the text content of the topic with flash card design as the background, paging buttons when content spans over one page, have media player bar at bottom to "play/pause/fast forward/reverse" audible
Nice to have
• i have 20 posters with quotes that inspires the user. i would like to see the posters to be presented full screen with a "inspire me" button somewhere which will randomly display a poster to the user.

```html
<!DOCTYPE html>
<html lang="en">
<head>
<meta charset="utf-8">
<title>Sharper Daily Habits – Topic Player</title>
<link href="https://fonts.googleapis.com/css2?family=Arimo:wght@400;700&display=swap" rel="stylesheet">
<style>
  :root {
    --teal: #3bbba3;
    --blue: #33a6d7;
    --ink: #111111;
    --muted: #555555;
    --track: #d9d9d9;
    --dot: #9a9a9a;
    --tabbar: #cfcfcf;
    --white: #ffffff;
  }
  * { margin: 0; padding: 0; box-sizing: border-box; }
  html, body { width: 675px; height: 1200px; overflow: hidden; background: var(--white); }
  body { font-family: "Arimo", Arial, sans-serif; color: var(--ink); position: relative; }

  .app-bar {
    position: absolute; left: 0; top: 0; width: 675px; height: 72px;
    background: var(--teal); color: var(--white);
    display: flex; align-items: center; justify-content: center;
  }
  .app-bar__title { font-size: 30px; font-weight: 700; }
  .app-bar__add { position: absolute; left: 14px; top: 16px; width: 40px; height: 40px; }

  .topic-heading {
    position: absolute; left: 0; top: 72px; width: 675px; height: 120px;
    display: flex; align-items: center; justify-content: center;
    font-size: 29px; font-weight: 700;
  }

  .topic-card {
    position: absolute; left: 0; top: 192px; width: 675px; height: 524px;
    background: linear-gradient(180deg, #0f3f93 0%, #2a6fbf 30%, #8fb4d4 47%, #c29a63 56%, #a97a47 72%, #3e3a36 100%);
  }

  .carousel-dots {
    position: absolute; left: 0; top: 740px; width: 675px;
    display: flex; justify-content: center; gap: 20px;
  }
  .carousel-dots span { width: 13px; height: 13px; border-radius: 50%; background: var(--dot); }
  .carousel-dots .is-active { background: var(--teal); }

  .progress { position: absolute; left: 0; top: 795px; width: 675px; height: 8px; background: var(--track); }
  .progress__fill { width: 472px; height: 100%; background: var(--blue); }
  .progress__head { position: absolute; left: 470px; top: -8px; width: 3px; height: 24px; background: var(--muted); }

  .time { position: absolute; top: 820px; font-size: 26px; color: var(--muted); }
  .time--elapsed { left: 20px; }
  .time--remaining { right: 20px; }

  .track-title { position: absolute; left: 0; top: 873px; width: 675px; text-align: center; font-size: 32px; }

  .controls { position: absolute; left: 0; top: 930px; width: 675px; height: 104px; }
  .controls__speed { position: absolute; left: 32px; top: 34px; font-size: 30px; }
  .controls svg { position: absolute; }

  .volume { position: absolute; left: 0; top: 1040px; width: 675px; height: 40px; }
  .volume svg { position: absolute; top: 4px; }
  .volume__line { position: absolute; left: 92px; top: 19px; width: 504px; height: 4px; background: #a8a8a8; border-radius: 2px; }
  .volume__line::before { content: ""; position: absolute; left: 0; top: 0; width: 342px; height: 4px; background: #777; }
  .volume__knob {
    position: absolute; left: 418px; top: 4px; width: 34px; height: 34px; border-radius: 50%;
    background: var(--white); border: 1px solid #bbb; box-shadow: 0 2px 4px rgba(0,0,0,.3);
  }

  .tab-bar {
    position: absolute; left: 0; top: 1112px; width: 675px; height: 88px; background: var(--tabbar);
    display: flex;
  }
  .tab { flex: 1; display: flex; flex-direction: column; align-items: center; padding-top: 12px; font-size: 17px; }
  .tab svg { width: 42px; height: 40px; margin-bottom: 6px; }
  .tab--active { color: var(--teal); }
</style>
</head>
<body>
  <header class="app-bar">
    <svg class="app-bar__add" viewBox="0 0 40 40"><path d="M20 4v32M4 20h32" stroke="#fff" stroke-width="6"/></svg>
    <h1 class="app-bar__title">Productivity</h1>
  </header>

  <h2 class="topic-heading">2. How to Avoid Distractions</h2>

  <div class="topic-card" role="img" aria-label="Topic card photo: a person walking down an empty desert road under a deep blue sky"></div>

  <div class="carousel-dots">
    <span></span><span class="is-active"></span><span></span><span></span><span></span><span></span><span></span><span></span>
  </div>

  <div class="progress"><div class="progress__fill"></div><div class="progress__head"></div></div>
  <span class="time time--elapsed">9:14</span>
  <span class="time time--remaining">-31:51</span>

  <p class="track-title">Habits of a Master - Marco Ellery</p>

  <div class="controls">
    <span class="controls__speed">1x</span>
    <svg style="left:128px;top:20px" width="68" height="68" viewBox="0 0 68 68">
      <path d="M18 18 A24 24 0 1 0 34 10" fill="none" stroke="#111" stroke-width="5"/>
      <path d="M34 1 L22 10 L34 19 Z" fill="#111"/>
      <text x="34" y="44" text-anchor="middle" font-family="Arimo, sans-serif" font-weight="700" font-size="19" fill="#111">30</text>
    </svg>
    <svg style="left:308px;top:16px" width="64" height="76" viewBox="0 0 64 76"><path d="M4 2 L62 38 L4 74 Z" fill="#111"/></svg>
    <svg style="left:479px;top:20px" width="68" height="68" viewBox="0 0 68 68">
      <path d="M50 18 A24 24 0 1 1 34 10" fill="none" stroke="#111" stroke-width="5"/>
      <path d="M34 1 L46 10 L34 19 Z" fill="#111"/>
      <text x="34" y="44" text-anchor="middle" font-family="Arimo, sans-serif" font-weight="700" font-size="19" fill="#111">30</text>
    </svg>
    <svg style="left:606px;top:38px" width="32" height="28" viewBox="0 0 32 28">
      <g fill="#111"><rect x="0" y="2" width="4" height="4"/><rect x="0" y="12" width="4" height="4"/><rect x="0" y="22" width="4" height="4"/>
      <rect x="8" y="2" width="24" height="4"/><rect x="8" y="12" width="24" height="4"/><rect x="8" y="22" width="24" height="4"/></g>
    </svg>
  </div>

  <div class="volume">
    <svg style="left:22px" width="24" height="32" viewBox="0 0 24 32"><path d="M2 11h7l9-8v26l-9-8H2z" fill="#555"/></svg>
    <div class="volume__line"></div>
    <div class="volume__knob"></div>
    <svg style="left:606px" width="40" height="32" viewBox="0 0 40 32"><path d="M2 11h7l9-8v26l-9-8H2z" fill="#555"/>
      <path d="M24 10q5 6 0 12M29 5q10 11 0 22" fill="none" stroke="#555" stroke-width="3"/></svg>
  </div>

  <nav class="tab-bar">
    <div class="tab tab--active">
      <svg viewBox="0 0 42 40"><g fill="#3bbba3"><rect x="4" y="26" width="34" height="9" rx="2"/><rect x="7" y="15" width="30" height="9" rx="2"/><rect x="5" y="4" width="32" height="9" rx="2"/></g></svg>
      My Library
    </div>
    <div class="tab">
      <svg viewBox="0 0 42 40"><circle cx="18" cy="16" r="11" fill="none" stroke="#111" stroke-width="5"/><path d="M26 24l11 11" stroke="#111" stroke-width="6"/></svg>
      Discover
    </div>
    <div class="tab">
      <svg viewBox="0 0 42 40"><path d="M21 2l5.6 12.5 13.4 1.3-10.1 9 3 13.2L21 31l-11.9 7 3-13.2-10.1-9 13.4-1.3z" fill="#111"/></svg>
      Topics
    </div>
    <div class="tab">
      <svg viewBox="0 0 42 40"><circle cx="21" cy="11" r="9" fill="#111"/><path d="M5 39c0-12 7-18 16-18s16 6 16 18z" fill="#111"/></svg>
      Me
    </div>
  </nav>
</body>
</html>
```